Office Suite Inspection Report

We are building a certification program for rent-able office space
And we need a document that we can supply as an inspection report.
This document, in most scenarios, is going to be co-branded with the landlord and is something that they can give their clients so that they fully understand the expected expenses that will be incurred by renting that location and will serve as an introduction to our company as a trusted provider of the types of services you need to run a modern cloud connected office.
We are working with landlords whom will provide us with the basic details of each of their rent-able office spaces so that we can outline the suitability of the space for networking services.
Document Outline
Desk Harbor Logo
Picture Of the rental space
Opening Text
Available Connectivity Options (
this should be a horizontal table of 3 to 4 options with the providers logo and 3-4 word description of the service and the price estimate )
Site Physical Inspection, this should be images and text about specific items of notice such as if there is a networking closet or room
We then want to offer pricing options for our services based on the expected number of users the office space should support
I have attached a presentation with a number of our services listed.
The following services are priced on a per user basis
Office / Productivity
Email
VoIP (Telephone Services)
Remote File Access
The following services are priced by location
Remote Backup
Network Services ( wired / wireless )
Ideally we can fit this on 2 - 3 pages
Connectivity Providers Logos -
Meridian Wave
https://www.findpix-example.test/search?q=meridian+wave+logo
Pell
https://www.findpix-example.test/search?q=pell+logo
QTNet
https://www.findpix-example.test/search?q=pell+logo#q=qtnet+logo

```html
<!DOCTYPE html>
<html lang="en">
<head>
<meta charset="utf-8">
<title>Services Price Per User Basis</title>
<link href="https://fonts.googleapis.com/css2?family=Oswald:wght@500;600&family=Titillium+Web:ital,wght@0,400;0,600;0,700;1,400&display=swap" rel="stylesheet">
<style>
  :root{
    --backdrop:#2a2a2a;
    --paper:#ffffff;
    --accent:#ec4423;
    --header:#0b3a52;
    --yellow:#fdd13f;
    --blue:#2d6cb0;
    --tag-blue:#3d58a6;
    --tag-lime:#c4d22f;
    --tag-olive:#5f5a22;
    --ink:#1d1d1d;
    --title-ink:#3a3a3a;
    --frame:#8a8a8a;
    --white:#ffffff;
  }
  *{box-sizing:border-box;margin:0;padding:0}
  html,body{width:1200px;height:1200px;overflow:hidden;background:var(--backdrop)}
  .page{
    position:absolute;left:138px;top:0;width:986px;height:1280px;
    transform:scale(.9375);transform-origin:0 0;
    background:var(--paper);
    font-family:"Titillium Web",sans-serif;color:var(--ink);
  }
  .page__bar{position:absolute;left:0;width:100%;height:10px;background:var(--accent)}
  .page__bar--top{top:0}
  .page__bar--bottom{bottom:0}

  .page-title{
    position:absolute;left:249px;top:28px;width:510px;height:57px;
    display:flex;align-items:center;justify-content:center;
    font-weight:700;font-size:32px;color:var(--title-ink);letter-spacing:.3px;
  }
  .page-title::before,.page-title::after{
    content:"";position:absolute;left:0;right:0;height:16px;
    border:2px solid var(--frame);
  }
  .page-title::before{top:0;border-bottom:none}
  .page-title::after{bottom:0;border-top:none}

  .service{position:absolute;left:49px;width:887px}
  .service__head{
    height:62px;background:var(--header);color:var(--white);
    font-family:"Oswald",sans-serif;font-weight:600;font-size:34px;
    display:flex;align-items:center;justify-content:center;letter-spacing:-.3px;
    position:relative;
  }
  .service__body{position:relative;border-radius:0 0 12px 12px}
  .service--yellow .service__body{background:var(--yellow);color:var(--ink)}
  .service--blue .service__body{background:var(--blue);color:var(--white)}

  .app-box{
    position:absolute;left:605px;top:12px;width:218px;height:43px;background:var(--white);
    display:flex;align-items:center;justify-content:center;gap:8px;
    font-family:"Titillium Web",sans-serif;font-size:15px;font-weight:600;color:var(--header);
  }
  .app-box__dot{width:12px;height:12px;background:var(--blue)}

  .tier{position:absolute;top:12px}
  .tier--left{left:20px}
  .tier--right{left:465px}
  .tier__row{display:flex;align-items:center;gap:15px}
  .tag{
    width:183px;height:36px;position:relative;
    display:flex;align-items:center;padding-left:44px;
    font-weight:700;font-size:19px;
    box-shadow:0 2px 0 rgba(0,0,0,.18);
  }
  .service--yellow .tag{background:var(--tag-blue);color:var(--white)}
  .service--blue .tag{background:var(--tag-lime);color:var(--tag-olive)}
  .tag__arrow{position:absolute;left:3px;top:6px;width:32px;height:24px}
  .price{font-weight:700;font-size:26px;line-height:1;display:flex;align-items:flex-start}
  .price sup{font-size:14px;margin-left:2px;margin-top:-2px}

  .features{list-style:none;position:absolute;top:74px;font-size:20px;line-height:24.8px}
  .features--left{left:27px;width:388px}
  .features--right{left:470px;width:410px}
  .features li{position:relative;padding-left:29px}
  .tick{position:absolute;left:0;top:3px;width:17px;height:17px}
  .service--yellow .tick{color:var(--ink)}
  .service--blue .tick{color:#cfe0f3}

  .note{position:absolute;left:473px;font-style:italic;font-size:20px;line-height:24.8px;color:var(--white)}
</style>
</head>
<body>
<svg width="0" height="0" style="position:absolute">
  <symbol id="tick" viewBox="0 0 20 20">
    <circle cx="9" cy="11" r="7.5" fill="none" stroke="currentColor" stroke-width="2"/>
    <path d="M5 11 l3.5 3.5 L18 3" fill="none" stroke="currentColor" stroke-width="2.4" stroke-linecap="round" stroke-linejoin="round"/>
  </symbol>
  <symbol id="arrow" viewBox="0 0 32 24">
    <path d="M1 1 H22 L31 12 L22 23 H1 Z" fill="#ffffff"/>
  </symbol>
</svg>

<main class="page">
  <div class="page__bar page__bar--top"></div>

  <h1 class="page-title">SERVICES PRICE/PER USER BASIS</h1>

  <section class="service service--yellow" style="top:115px">
    <h2 class="service__head"><span style="margin-left:-150px">OFFICE/PRODUCTIVITY</span>
      <span class="app-box"><span class="app-box__dot"></span>Quillfern Apps</span>
    </h2>
    <div class="service__body" style="height:205px">
      <div class="tier tier--left"><div class="tier__row">
        <span class="tag"><svg class="tag__arrow"><use href="#arrow"/></svg>STANDARD</span>
        <span class="price">$15<sup>.00</sup></span></div></div>
      <div class="tier tier--right"><div class="tier__row">
        <span class="tag"><svg class="tag__arrow"><use href="#arrow"/></svg>POWER USERS</span>
        <span class="price">$30<sup>.00</sup></span></div></div>
      <ul class="features features--left">
        <li><svg class="tick"><use href="#tick"/></svg>Quillfern Office Suite licensing</li>
        <li><svg class="tick"><use href="#tick"/></svg>Application installation and updates</li>
      </ul>
      <ul class="features features--right">
        <li><svg class="tick"><use href="#tick"/></svg>All the features of Productivity – Standard</li>
        <li><svg class="tick"><use href="#tick"/></svg>Additional 20+ Business-class Applications</li>
        <li><svg class="tick"><use href="#tick"/></svg>Web, Utilities, Messaging, Media, Runtimes,</li>
        <li><svg class="tick"><use href="#tick"/></svg>Compression, Imaging, Documents, Security, Tools, Online Storage</li>
      </ul>
    </div>
  </section>

  <section class="service service--blue" style="top:400px">
    <h2 class="service__head">EMAIL</h2>
    <div class="service__body" style="height:196px">
      <div class="tier tier--left"><div class="tier__row">
        <span class="tag"><svg class="tag__arrow"><use href="#arrow"/></svg>STANDARD</span>
        <span class="price">$15<sup>.00</sup></span></div></div>
      <div class="tier tier--right"><div class="tier__row">
        <span class="tag"><svg class="tag__arrow"><use href="#arrow"/></svg>POWER USERS</span>
        <span class="price">$30<sup>.00</sup></span></div></div>
      <ul class="features features--left">
        <li><svg class="tick"><use href="#tick"/></svg>Business-class email with 50 GB mailbox</li>
        <li><svg class="tick"><use href="#tick"/></svg>SPAM filtering and virus protection</li>
        <li><svg class="tick"><use href="#tick"/></svg>Quillfern Mail and mobile device support</li>
        <li><svg class="tick"><use href="#tick"/></svg>Administration of users and email server</li>
      </ul>
      <ul class="features features--right">
        <li><svg class="tick"><use href="#tick"/></svg>All the features of Email – Standard</li>
        <li><svg class="tick"><use href="#tick"/></svg>Unlimited email storage for in-place archive</li>
        <li><svg class="tick"><use href="#tick"/></svg>Archiving and legal hold</li>
      </ul>
    </div>
  </section>

  <section class="service service--yellow" style="top:681px">
    <h2 class="service__head">UNIFIED COMMUNICATIONS - VOIP</h2>
    <div class="service__body" style="height:202px">
      <div class="tier tier--left"><div class="tier__row">
        <span class="tag"><svg class="tag__arrow"><use href="#arrow"/></svg>STANDARD</span>
        <span class="price">$25<sup>.00</sup></span></div></div>
      <div class="tier tier--right"><div class="tier__row">
        <span class="tag"><svg class="tag__arrow"><use href="#arrow"/></svg>POWER USERS</span>
        <span class="price">$30<sup>.00</sup></span></div></div>
      <ul class="features features--left">
        <li><svg class="tick"><use href="#tick"/></svg>Business-class phone service with<br>unlimited calling</li>
        <li><svg class="tick"><use href="#tick"/></svg>Includes 30+ features</li>
        <li><svg class="tick"><use href="#tick"/></svg>Extended mobility features</li>
      </ul>
      <ul class="features features--right">
        <li><svg class="tick"><use href="#tick"/></svg>All the features of User – Standard</li>
        <li><svg class="tick"><use href="#tick"/></svg>Call Recording</li>
        <li><svg class="tick"><use href="#tick"/></svg>Personal Fax box</li>
        <li><svg class="tick"><use href="#tick"/></svg>Personal Music On Hold</li>
        <li><svg class="tick"><use href="#tick"/></svg>Personal Conference Bridge</li>
      </ul>
    </div>
  </section>

  <section class="service service--blue" style="top:970px">
    <h2 class="service__head">FILE SHARING &amp; CLOUD ACCESS</h2>
    <div class="service__body" style="height:221px">
      <div class="tier tier--left"><div class="tier__row">
        <span class="tag"><svg class="tag__arrow"><use href="#arrow"/></svg>STANDARD</span>
        <span class="price">$15<sup>.00</sup></span></div></div>
      <div class="tier tier--right"><div class="tier__row">
        <span class="tag"><svg class="tag__arrow"><use href="#arrow"/></svg>POWER USERS</span>
        <span class="price">$30<sup>.00</sup></span></div></div>
      <ul class="features features--left">
        <li><svg class="tick"><use href="#tick"/></svg>Business-class file sharing with real-time<br>cloud sync*</li>
        <li><svg class="tick"><use href="#tick"/></svg>Automatic file versioning</li>
        <li><svg class="tick"><use href="#tick"/></svg>Define user permissions for each share</li>
        <li>Administration of users and site storage appliance</li>
      </ul>
      <ul class="features features--right">
        <li><svg class="tick"><use href="#tick"/></svg>All the features of File Sharing – Standard</li>
        <li><svg class="tick"><use href="#tick"/></svg>Access shares anywhere via Network Drives</li>
      </ul>
      <p class="note" style="top:131px">Use your files in the cloud via office online<br>when you pair withour productivity offering</p>
      <p class="note" style="top:187px">* Requires Site Storage Appliance</p>
    </div>
  </section>

  <div class="page__bar page__bar--bottom"></div>
</main>
</body>
</html>
```